Harbor Sushi & Steak Dinner Menu

I'm looking for a MENU design with a particular feel. I want to have a base template made that I can then use for future alterations to the menu; ie I can go in and change out different entrees as the menu changes but the template will remain the same. (Ideally it would be in an Apple Pages format.). Also ideally - dinner menu will occupy 2 pages 8.5 x 11. The restaurant's name is Harbor. It is a MODERN steak house that will also feature Sushi, a Raw Bar, Exquisite Cocktails and a sophisticated nightlife crowd. I have attached our LOGO, a secondary logo that we will be featuring throughout the project including on the menu cover (the gold U). Finally - I have attached the content that we would like to see. AGAIN - I REITERATE: High end dining and lounge atmosphere. A couple of restaurants / menus that I love are Morvendel in NYC and Pellucid Steakhouse in Long Island NY. Please do not duplicate - just trying to offer some suggestions.

Requirements
Must have
• A sophisticated and elegant feel without being stuffy or old.

```html
<!DOCTYPE html>
<html lang="en">
<head>
<meta charset="utf-8">
<title>Harbor Sushi &amp; Steak — Dinner Menu</title>
<link href="https://fonts.googleapis.com/css2?family=EB+Garamond:ital,wght@0,400;0,500;1,400&display=swap" rel="stylesheet">
<style>
  :root{
    --backdrop:#3c3e42;
    --paper:#efefef;
    --slate:#2a2a2b;
    --slate-deep:#1f1f20;
    --gold:#d8bf7a;
    --wine:#c23a4e;
    --ink:#e9e6e0;
    --ink-soft:#c9c5bd;
    --photo-light:#5b4a40;
    --photo-dark:#3a322e;
  }
  *{box-sizing:border-box;margin:0;padding:0}
  html,body{width:1200px;height:900px;overflow:hidden}
  body{background:var(--backdrop);font-family:"EB Garamond",Georgia,serif;color:var(--ink);position:relative}

  .sheet{position:absolute;background:var(--paper);padding:14px}
  .page{width:100%;height:100%;background:linear-gradient(160deg,#343435 0%,var(--slate) 45%,var(--slate-deep) 100%);position:relative;overflow:hidden}

  .spread{position:absolute;left:24px;top:191px;width:800px;height:518px;display:flex}
  .spread .sheet{position:relative;width:400px;height:518px}
  .spread .sheet:first-child{border-right:1px solid #d6d6d6}

  .wordmark{display:flex;align-items:center;justify-content:center;gap:7px;color:var(--gold);font-weight:400;letter-spacing:.22em;text-transform:uppercase}
  .wordmark .dot{width:7px;height:7px;border-radius:50%;background:var(--wine);flex:none}
  .page-head{height:62px;padding-top:20px}
  .page-head .wordmark{font-size:24px}

  .columns{display:flex;gap:12px;padding:0 14px 0 18px}
  .col{flex:1;min-width:0}
  .section{margin-bottom:7px}
  .section h2{font-size:10.5px;font-weight:500;color:var(--gold);text-transform:uppercase;letter-spacing:.02em;line-height:1.1;margin-bottom:1px}
  .item{font-size:6.9px;line-height:1.22;color:var(--ink)}
  .item i{color:var(--ink-soft)}
  .item.gold i{color:var(--gold)}

  .covers{position:absolute;left:852px;top:22px;width:324px}
  .covers .sheet{position:relative;width:324px;height:418px;margin-bottom:20px}
  .cover-back .page{display:flex;flex-direction:column;align-items:center}
  .cover-back .wordmark{font-size:40px;margin-top:160px}
  .cover-back .thanks{position:absolute;bottom:26px;left:0;right:0;text-align:center;color:var(--gold);font-size:15px;text-transform:uppercase;letter-spacing:.02em}

  .cover-front .page{display:flex;flex-direction:column;align-items:center}
  .cover-front .wordmark{font-size:30px;margin-top:38px}
  .cover-front .photo{width:150px;height:112px;margin-top:42px;background:linear-gradient(160deg,var(--photo-light),var(--photo-dark))}
  .menu-title{margin-top:36px;text-align:center}
  .menu-title .rule{width:122px;height:1px;background:var(--gold);margin:0 auto}
  .menu-title h1{font-size:34px;font-weight:500;color:var(--gold);line-height:1.15;padding:3px 0}
  .menu-title p{font-size:9px;color:var(--wine);text-transform:uppercase;margin-top:6px}
</style>
</head>
<body>

<div class="spread">
  <div class="sheet">
    <div class="page">
      <div class="page-head"><div class="wordmark"><span class="dot"></span>Harbor</div></div>
      <div class="columns">
        <div class="col">
          <div class="section">
            <h2>Sushi / Sashimi</h2>
            <p class="item">Toro; <i>blue fin tuna belly (gf)</i></p>
            <p class="item">Unagi; <i>fresh water eel (gf)</i></p>
            <p class="item">Ebi; <i>cooked shrimp (gf)</i></p>
            <p class="item">Sake; <i>salmon (gf)</i></p>
            <p class="item">Hamachi; <i>yellowtail (gf)</i></p>
            <p class="item">Madai; <i>red snapper (gf)</i></p>
            <p class="item">Uni; <i>sea urchin (gf)</i></p>
            <p class="item">Maguro; <i>tuna (gf)</i></p>
            <p class="item">Hirame; <i>fluke (gf)</i></p>
          </div>
          <div class="section">
            <h2>Sushi Platters</h2>
            <p class="item">Small: <i>Five Pieces assorted sushi, nine pieces sashimi, spicy tuna roll (gf)</i></p>
            <p class="item">Large: <i>Eight Pieces assorted sushi, eighteen pieces of sashimi, alaskan roll, rainbow roll (gf)</i></p>
          </div>
          <div class="section">
            <h2>Classic Rolls</h2>
            <p class="item">Yellowtail; <i>inside out roll with scallions (gf)</i></p>
            <p class="item">Spicy Tuna or Salmon or Yellowtail; <i>spicy mayo</i></p>
            <p class="item">California: <i>crab meat, cucumber and avocado (gf)</i></p>
            <p class="item">Vegetable: <i>avocado, cucumber, asparagus and pickled reddish (gf)</i></p>
            <p class="item">Spider: <i>soft shell crab and avocado with eel sauce</i></p>
            <p class="item">Shrimp Tempura: <i>deep fried tempura shrimp and eel sauce</i></p>
            <p class="item">Alaskan; <i>salmon and avocado (gf)</i></p>
          </div>
          <div class="section">
            <h2>Special Rolls</h2>
            <p class="item">The Harbor: <i>tuna, salmon, yellowtail, avocado, spicy mayo, soy bean paper</i></p>
            <p class="item">King Crab Rainbow: <i>king crab, avocado, cucumbers, assorted fish on top</i></p>
            <p class="item">Empress: <i>Shrimp tempura, spicy tuna on top, eel sauce, spicy mayo</i></p>
            <p class="item">Spicy Girl: <i>Spicy crunchy crab meat, cucumber, shrimp on top</i></p>
          </div>
        </div>
        <div class="col">
          <div class="section">
            <p class="item">Dragon: <i>Eel, cucumber, avocado, and tobiko on top, eel sauce</i></p>
            <p class="item">Yummy: <i>spicy crunchy salmon, avocado, mango and salmon on top</i></p>
            <p class="item">No. 9: <i>Shrimp Tempura, avocado, kani, spicy mayo, tobiko</i></p>
            <p class="item">Sunrise Roll: <i>spicy crunchy tuna and avocado, spicy crunchy salmon on top</i></p>
          </div>
          <div class="section">
            <h2>Seafood Raw Bar</h2>
            <p class="item">Lobster Cocktail</p>
            <p class="item">Shrimp Cocktail</p>
            <p class="item">Clams on the Half Shell</p>
            <p class="item">Oysters on the Half Shell</p>
            <p class="item">Colossal Crab Cocktail</p>
            <p class="item">Raw Bar Plate for One: <i>Two Shrimp, Half of a One Pound Lobster, Two Clams, One East Coast Oyster, One West Coast Oyster</i></p>
          </div>
          <div class="section">
            <h2>Apps</h2>
            <p class="item">BAO Bun: <i>hoisin bbq pancetta cut pork loin, crispy onions, micro mint</i></p>
            <p class="item">Five Spice Crispy Popcorn Crusted Prawns (2); <i>classic burre blanc</i></p>
            <p class="item">Jumbo Lump Crab; <i>citrus miso drizzle, spring pea puree, micro greens</i></p>
            <p class="item">Crispy Wonton Napoleon; <i>cucumber gallete, ahi tuna, jumbo lump crab meat, wasabi aioli, shoestring wontons</i></p>
            <p class="item">PEI Mussels; <i>charred artichoke hearts, blistered heirloom tomatoes, garlic white wine broth</i></p>
            <p class="item">New Zealand or Domestic Small Eye Lamb Chop (1); <i>crispy porcini risotto cake</i></p>
          </div>
          <div class="section">
            <h2>Seafood Platters (gf)</h2>
            <p class="item gold">Shrimp, Oysters, Clams, Lobster and Crab <i>Large or Colossal</i></p>
          </div>
        </div>
      </div>
    </div>
  </div>

  <div class="sheet">
    <div class="page">
      <div class="page-head"><div class="wordmark"><span class="dot"></span>Harbor</div></div>
      <div class="columns">
        <div class="col">
          <div class="section">
            <h2>Salads</h2>
            <p class="item">Classic Wedge; <i>bleu cheese, bacon lardons, heirloom tomatoes</i></p>
            <p class="item">Mixed Baby Greens; <i>heirloom tomatoes, cucumber, red onion, dijon vinaigrette</i></p>
            <p class="item">Tabulleh; <i>buckwheat grain, fresh mint, tomato concasse, cucumber, parsley, fresh squeezed lemon, EVOO, salt and pepper</i></p>
            <p class="item">Tomato Mozzarella Salad / Burratta</p>
            <p class="item">Spinach Salad; <i>green apple, feta, currants, with per-simmons vinaigrette</i></p>
            <p class="item">Kale Caesar; <i>homemade cacio e'peppe dressing, pecorino and parmesan cheese, toasted croutons</i></p>
          </div>
          <div class="section">
            <h2>Entrees</h2>
            <p class="item">Pan Roasted Miso Glazed Black Cod; <i>green tea noodle stir fry; Napa cabbage, carrot, Japanese eggplant</i></p>
            <p class="item">Pan Seared Striped Bass; <i>lobster succotash in a tomato saffron broth</i></p>
            <p class="item">E.V.O.O. Salted / Grilled Swordfish; <i>sun dried tomato, olive and caper tapenade, over basmati rice</i></p>
            <p class="item">Grilled Half Chicken; <i>sun dried tomato and basil Israeli cous-cous, pan au jus</i></p>
            <p class="item">Roasted Fresh Caviatelle Ratatoille; <i>vegetable broth</i></p>
            <p class="item">Lobster Cartoccio; <i>shrimp, mussels, clams, fresh herb tomato broth, tossed with bucatini</i></p>
            <p class="item">Charred Artichoke Hearts, <i>heirloom tomatoes, caper berries, spring onions, fresh basil, white wine reduction over forbidden rice (gf)</i></p>
            <p class="item">Mediterranean Grilled Veggie Plate; <i>artichoke hearts, Japanese eggplant, green &amp; white asparagus, seared heirloom tomatoes, roasted baby carrots, cauliflower rice, evoo &amp; fig drizzle (gf)</i></p>
          </div>
        </div>
        <div class="col">
          <div class="section">
            <h2>USDA Prime Steaks (gf)</h2>
            <p class="item">10 Oz Filet</p>
            <p class="item">14 or 16 oz New York Strip</p>
            <p class="item">24 oz Boneless Ribeye</p>
            <p class="item">36 oz Bone in Rib Eye</p>
            <p class="item">Berkshire Pork Chop</p>
          </div>
          <div class="section">
            <h2>Sauces</h2>
            <p class="item">Cabernet Demi Glaz</p>
            <p class="item">Gorganzola Brulle Cream</p>
            <p class="item">Truffled Wild Mushroom Ragu</p>
            <p class="item">Horseradish Cream</p>
            <p class="item">House Steak Sauce</p>
          </div>
          <div class="section">
            <h2>Sides</h2>
            <p class="item">Mashed Idaho Potatoes</p>
            <p class="item">Bacon, Sweet Corn, Caramelized Vidalia Onion fingerling potatoes</p>
            <p class="item">Roasted Peanut Potatoes</p>
            <p class="item">Creamed Spinach</p>
            <p class="item">Sautéed Spinach</p>
            <p class="item">Grilled Asparagus</p>
            <p class="item">French Beans</p>
            <p class="item">Israeli Cous Cous</p>
            <p class="item">Sweet Potato Steak Fries</p>
            <p class="item">Corn Skillet</p>
          </div>
          <div class="section">
            <h2>Desserts</h2>
            <p class="item">T.B.D. - separate menu</p>
          </div>
        </div>
      </div>
    </div>
  </div>
</div>

<div class="covers">
  <div class="sheet cover-back">
    <div class="page">
      <div class="wordmark"><span class="dot"></span>Harbor</div>
      <p class="thanks">Thank you for visiting!</p>
    </div>
  </div>
  <div class="sheet cover-front">
    <div class="page">
      <div class="wordmark"><span class="dot"></span>Harbor</div>
      <div class="photo" role="img" aria-label="Photograph of grilled steaks with a rosemary sprig"></div>
      <div class="menu-title">
        <div class="rule"></div>
        <h1>MENU</h1>
        <div class="rule"></div>
        <p>Rich food menu for every taste!</p>
      </div>
    </div>
  </div>
</div>

</body>
</html>
```